Web form face-lift for an online startup

We are a web startup building a SaaS application for the freight industry. The project is mainly dedicated to the paint the main form that our customer are using along the search results that the they get. All details are in the attached documents.
Updates
The application serves the Freight Forwarders community so please think towards this industry when using background images, banners, colors, icons, etc. Computer and technology images are irrelevant.
Customer fields at the top of the page is actually part of the form.
Target Market(s)
Usually business users (Sales people, procurement, shippers, freight forwarders). Some are less tech savvy and some appreciate the new trendy web apps.
Industry/Entity Type
Building
Colors
Designer to choose colors to be used in the design.
Look and feel
Each slider illustrates characteristics of the customer's brand and the style your logo design should communicate.

```html
<!DOCTYPE html>
<html lang="en">
<head>
<meta charset="utf-8">
<title>CargoQuotely – Search For Quotes</title>
<link href="https://fonts.googleapis.com/css2?family=Lato:wght@400;700&family=Oswald:wght@400;500&display=swap" rel="stylesheet">
<style>
:root{
  --brand:#0a4f9c;
  --brand-light:#0d63bf;
  --band:#c8dff4;
  --ink:#333;
  --muted:#555;
  --line:#dcdcdc;
  --field:#fff;
  --select:#d9d9d9;
  --footer:#262626;
  --danger:#e0161b;
}
*{box-sizing:border-box;margin:0;padding:0}
html,body{width:1200px;height:1077px;overflow:hidden;background:#fff}
body{position:relative;font-family:"Lato",sans-serif;color:var(--ink);font-size:14px}
.abs{position:absolute}
.btn{position:absolute;display:flex;align-items:center;justify-content:center;color:#fff;background:linear-gradient(#0d5fb6,#0a4a94);border-radius:2px;font-family:"Lato",sans-serif}
.field{position:absolute;background:var(--field);border:1px solid #d4d4d4;border-radius:2px;font-size:12px;display:flex;align-items:center;padding-left:10px;color:#222;font-family:Arial,sans-serif}
.field.center{justify-content:center;padding-left:0}
.select{position:absolute;background:var(--select);border-radius:2px;font-size:12px;display:flex;align-items:center;padding-left:12px;color:#333;font-family:Arial,sans-serif}
.select::after{content:"";position:absolute;right:12px;top:50%;margin-top:-3px;border:5px solid transparent;border-top:6px solid #444;border-bottom:0}
.dropdown{position:absolute;background:#fff;border:1px solid #ccc;border-radius:2px;font-size:12px;display:flex;align-items:center;padding-left:9px;font-family:Arial,sans-serif}
.dropdown::after{content:"";position:absolute;right:10px;top:50%;margin-top:-2px;border:5px solid transparent;border-top:6px solid #444;border-bottom:0}
.check{position:absolute;width:15px;height:15px;background:#fff;border:1px solid #ccc}
.header{position:absolute;left:0;top:0;width:1200px;height:108px;border-bottom:1px solid #c9d6e2;box-shadow:0 1px 3px rgba(0,0,0,.08)}
.brand-name{left:114px;top:38px;font-family:"Lato",sans-serif;font-weight:700;font-size:30px;color:var(--brand);line-height:1}
.nav a{position:absolute;top:66px;height:29px;line-height:29px;color:#222;text-decoration:none;font-size:14px}
.nav a.active{background:linear-gradient(#0d5fb6,#0a4a94);color:#fff;border-radius:2px;text-align:center}
.band{position:absolute;left:0;width:1200px;background:var(--band)}
.h2{position:absolute;font-family:"Oswald",sans-serif;font-weight:400;color:var(--brand);font-size:26px;line-height:1}
.label{position:absolute;font-size:16px;color:#444}
.tab{position:absolute;top:315px;height:70px;background:linear-gradient(#353535,#1e1e1e);display:flex;align-items:center;justify-content:center;border-top:1px solid #555}
.tab.active{background:linear-gradient(#1565c0,#0a4a94);border-top:0}
.tab.active::after{content:"";position:absolute;bottom:-1px;left:50%;margin-left:-7px;border:7px solid transparent;border-bottom-color:#fff;border-top:0}
.panel{position:absolute;left:112px;top:385px;width:975px;height:267px;border:1px solid var(--line);border-bottom:0}
.colhead{position:absolute;top:408px;font-size:14px;font-weight:700;color:#444}
.total{position:absolute;left:665px;top:590px;font-size:14px;font-weight:700;color:#444}
.opt{position:absolute;top:817px;font-size:16px;color:#555}
.radio{position:absolute;top:818px;width:19px;height:19px;border:1px solid #ccc;border-radius:50%;background:#fff}
.hazard{position:absolute;top:812px}
.footer{position:absolute;left:0;top:1021px;width:1200px;height:56px;background:var(--footer)}
.footer a{position:absolute;top:20px;color:#fff;text-decoration:none;font-size:14px}
.sep{position:absolute;top:25px;width:7px;height:7px;background:
 radial-gradient(circle,#777 1.2px,transparent 1.4px) 0 0/3.5px 3.5px}
.social{position:absolute;top:17px;width:22px;height:22px;border-radius:2px;background:#5a5a5a}
</style>
</head>
<body>

<header class="header">
  <div class="abs brand-name">CargoQuotely</div>
  <div class="dropdown" style="left:818px;top:19px;width:66px;height:28px">USD</div>
  <div class="dropdown" style="left:894px;top:19px;width:81px;height:28px">English</div>
  <div class="btn" style="left:985px;top:19px;width:102px;height:29px;font-size:14px">USER NAME</div>
  <nav class="nav">
    <a class="active" style="left:452px;width:109px">Menu Item1</a>
    <a style="left:579px">Menu Item2</a>
    <a style="left:688px">Menu Item3</a>
    <a style="left:797px">Menu Item4</a>
    <a style="left:906px">Menu Item5</a>
    <a style="left:1014px">Menu Item6</a>
  </nav>
</header>

<section class="band" style="top:109px;height:160px">
  <div class="h2" style="left:112px;top:19px">Search For Quotes</div>
  <div class="label" style="left:113px;top:72px">Customer</div>
  <div class="field" style="left:197px;top:64px;width:293px;height:37px;border:0"></div>
  <div class="check" style="left:112px;top:121px;width:12px;height:12px;border:0"></div>
  <div class="label" style="left:134px;top:117px">Rate Quotes ?</div>
</section>

<div class="tab active" style="left:112px;width:104px">
  <svg width="48" height="42" viewBox="0 0 48 42"><path d="M24 2 45 11 24 20 3 11Z" fill="#fff"/><path d="M3 14 22 22V40L3 32Z M45 14 26 22V40L45 32Z" fill="#fff"/><path d="M14 6.5 35 15.5V20" stroke="#0d5fb6" stroke-width="2" fill="none"/></svg>
</div>
<div class="tab" style="left:220px;width:103px">
  <svg width="50" height="42" viewBox="0 0 50 42"><path d="M4 10 30 4 46 10V34L30 40 4 34Z" fill="#888"/><path d="M30 4V40" stroke="#555" stroke-width="2"/><g stroke="#666" stroke-width="1.5"><path d="M8 11V33M12 10V34M16 9V35M20 8V36M24 7V37"/><path d="M34 11V33M38 12V32M42 13V31"/></g></svg>
</div>
<div class="tab" style="left:328px;width:103px">
  <svg width="42" height="42" viewBox="0 0 42 42"><g fill="#8a8a8a"><path d="M14 2 21 5 14 8 7 5Z M28 2 35 5 28 8 21 5Z"/><path d="M5 8 19 14V26L5 20Z M37 8 23 14V26L37 20Z"/><path d="M5 23 19 29V40L5 34Z M37 23 23 29V40L37 34Z"/></g></svg>
</div>
<div class="btn" style="left:1023px;top:336px;width:64px;height:29px;font-size:14px;font-weight:700">More ››</div>

<section class="panel" aria-label="Cargo units"></section>
<div class="colhead" style="left:150px">Qty</div>
<div class="colhead" style="left:212px">Stackable</div>
<div class="colhead" style="left:307px">Load</div>
<div class="colhead" style="left:583px">Length</div>
<div class="colhead" style="left:670px">Width</div>
<div class="colhead" style="left:748px">Height</div>
<div class="colhead" style="left:916px">Weight</div>

<div class="field center" style="left:142px;top:441px;width:38px;height:35px">5</div>
<div class="check" style="left:232px;top:451px"></div>
<div class="select" style="left:304px;top:441px;width:244px;height:35px">Box/Pallet</div>
<div class="field center" style="left:576px;top:441px;width:57px;height:35px">100</div>
<div class="field center" style="left:660px;top:441px;width:57px;height:35px">100</div>
<div class="field center" style="left:744px;top:441px;width:53px;height:35px">100</div>
<div class="select" style="left:823px;top:441px;width:64px;height:35px">cm</div>
<div class="field center" style="left:914px;top:441px;width:53px;height:35px">100</div>
<div class="select" style="left:995px;top:441px;width:63px;height:35px">kg</div>

<div class="btn" style="left:142px;top:504px;width:153px;height:38px;font-size:14px;justify-content:flex-start;padding-left:12px">
  <svg width="12" height="12" viewBox="0 0 12 12" style="margin-right:11px"><path d="M6 0V12M0 6H12" stroke="#fff" stroke-width="1.6"/></svg>ADD MORE UNIT
</div>
<div class="abs" style="left:142px;top:561px;width:915px;border-top:1px dashed #ddd"></div>

<div class="total">Total</div>
<div class="field center" style="left:711px;top:580px;width:52px;height:36px">5</div>
<div class="field center" style="left:782px;top:580px;width:62px;height:36px">1</div>
<div class="select" style="left:843px;top:580px;width:71px;height:36px">CBM</div>
<div class="field center" style="left:933px;top:580px;width:62px;height:36px">100</div>
<div class="select" style="left:994px;top:580px;width:64px;height:36px">kg</div>

<section class="band" style="top:651px;height:66px">
  <div class="abs" style="left:123px;top:27px;font-size:14px;font-weight:700;color:#444">From :</div>
  <div class="field" style="left:178px;top:17px;width:385px;height:35px;border:0">Shipping address or port</div>
  <svg class="abs" style="left:591px;top:26px" width="34" height="16" viewBox="0 0 34 16"><path d="M0 5H22V0L34 8 22 16V11H0Z" fill="var(--brand)"/></svg>
  <div class="abs" style="left:653px;top:27px;font-size:14px;font-weight:700;color:#444">To :</div>
  <div class="field" style="left:690px;top:17px;width:385px;height:35px;border:0">Shipping address or port</div>
</section>

<section aria-label="Options">
  <div class="h2" style="left:114px;top:742px">Options</div>
  <svg class="abs" style="left:112px;top:781px" width="975" height="14" viewBox="0 0 975 14"><path d="M0 6.5H15L22 13 29 6.5H975" stroke="#ccc" fill="#fff"/></svg>

  <div class="radio" style="left:112px"></div><div class="opt" style="left:142px">Import</div>
  <div class="radio" style="left:220px"></div><div class="opt" style="left:251px">Export</div>
  <div class="opt" style="left:330px">Incoterm:</div>
  <div class="opt" style="left:405px;color:var(--brand);font-weight:700">FCA</div>

  <div class="check" style="left:553px;top:820px"></div>
  <svg class="hazard" style="left:577px" width="30" height="30" viewBox="0 0 30 30"><circle cx="15" cy="15" r="13.5" fill="#fff" stroke="var(--danger)" stroke-width="2.5"/><path d="M9 9 15 7 21 9V15C21 19 18 22 15 23 12 22 9 19 9 15Z" fill="#333"/><path d="M5.5 5.5 24.5 24.5" stroke="var(--danger)" stroke-width="2.5"/></svg>
  <div class="check" style="left:624px;top:820px"></div>
  <svg class="hazard" style="left:649px" width="30" height="30" viewBox="0 0 30 30"><circle cx="15" cy="15" r="13.5" fill="#fff" stroke="var(--danger)" stroke-width="2.5"/><circle cx="15" cy="11" r="4" fill="#333"/><path d="M8 23C8 18 11 16 15 16 19 16 22 18 22 23Z" fill="#333"/><path d="M5.5 5.5 24.5 24.5" stroke="var(--danger)" stroke-width="2.5"/></svg>
  <div class="check" style="left:696px;top:820px"></div>
  <svg class="hazard" style="left:720px" width="30" height="30" viewBox="0 0 30 30"><circle cx="15" cy="15" r="13.5" fill="#fff" stroke="var(--danger)" stroke-width="2.5"/><g fill="#333"><path d="M15 15 10 7A9 9 0 0 1 20 7Z"/><path d="M15 15 24 15A9 9 0 0 1 19.5 23Z"/><path d="M15 15 10.5 23A9 9 0 0 1 6 15Z"/></g><circle cx="15" cy="15" r="2" fill="#fff"/><path d="M5.5 5.5 24.5 24.5" stroke="var(--danger)" stroke-width="2.5"/></svg>

  <div class="select" style="left:843px;top:810px;width:244px;height:36px">Price Level</div>
  <div class="btn" style="left:951px;top:864px;width:136px;height:38px;font-size:14px">MORE OPTIONS ››</div>
</section>

<div class="btn" style="left:400px;top:940px;width:211px;height:43px;font-size:20px;font-weight:700">SEARCH QUOTES</div>
<div class="abs" style="left:635px;top:953px;font-size:15px;color:#555">OR</div>
<div class="abs" style="left:686px;top:952px;font-size:16px;font-weight:700;color:var(--brand)">Create manually</div>

<footer class="footer">
  <a style="left:114px">About Us</a><span class="sep" style="left:187px"></span>
  <a style="left:208px">Privacy Policy</a><span class="sep" style="left:316px"></span>
  <a style="left:331px">Terms of Service</a><span class="sep" style="left:458px"></span>
  <a style="left:468px">News</a>
  <span class="social" style="left:933px" role="img" aria-label="Blog link"></span>
  <span class="social" style="left:966px" role="img" aria-label="Social link"></span>
  <span class="social" style="left:999px" role="img" aria-label="Social link"></span>
  <span class="social" style="left:1032px" role="img" aria-label="Social link"></span>
  <span class="social" style="left:1065px" role="img" aria-label="Video channel link"></span>
</footer>

</body>
</html>
```